Brochure required

Looking at getting business brochure designed for my solar sales company. i will require a range of products to be listed on the brochure I require a simple/ elegent / professional looking brochure.

I am happy to provide designer with all the required information that must go into the brochure. otherwise please visit www.velorquintade.com.au and view the products which i would like to allocate into the brochure aswell as our company logo and a little about me section

```html
<!DOCTYPE html>
<html lang="en">
<head>
<meta charset="utf-8">
<title>Velorquintade – Energy solutions for a changing world</title>
<link rel="stylesheet" href="https://fonts.googleapis.com/css2?family=Montserrat:wght@800&family=Arimo:wght@400&family=Roboto+Condensed:wght@700&family=Yellowtail&display=swap">
<style>
  :root {
    --ink: #111a2b;
    --white: #ffffff;
    --band-yellow: #e2c42c;
    --band-green: #13b98b;
    --band-blue: #1692b8;
    --brand-square: #e2c42c;
    --sky-top: #4a6f86;
    --sky-mid: #6f8ea2;
    --panel-mid: #3a4a78;
    --panel-deep: #141a33;
  }
  * { margin: 0; padding: 0; box-sizing: border-box; }
  html, body { width: 1200px; height: 927px; overflow: hidden; background: var(--white); }
  .brochure-cover { position: relative; width: 1200px; height: 927px; overflow: hidden; }

  .masthead { position: absolute; left: 0; top: 0; width: 1200px; height: 126px; background: var(--white); }
  .brand { position: absolute; left: 18px; top: 30px; display: flex; align-items: center; gap: 12px; }
  .brand-square { width: 34px; height: 34px; background: var(--brand-square); }
  .brand-name {
    font-family: "Montserrat", sans-serif; font-weight: 800; font-size: 46px;
    color: var(--ink); letter-spacing: -0.5px; line-height: 1;
  }
  .contact {
    position: absolute; left: 795px; top: 38px; width: 370px;
    font-family: "Arimo", Arial, sans-serif; font-size: 27px; line-height: 34px; color: var(--ink);
    white-space: nowrap;
  }

  .hero-photo {
    position: absolute; left: 0; top: 126px; width: 1200px; height: 801px;
    background: linear-gradient(180deg, var(--sky-top) 0%, var(--sky-mid) 28%, #54698a 45%, var(--panel-mid) 58%, #27305a 78%, var(--panel-deep) 100%);
  }

  .headline {
    position: absolute; left: 55px; right: 0; top: 330px;
    font-family: "Roboto Condensed", "Arial Narrow", sans-serif; font-weight: 700;
    font-size: 110px; line-height: 137px; color: var(--white); text-align: center;
    letter-spacing: -1px;
  }

  .tagline { position: absolute; left: 0; top: 700px; width: 1200px; height: 112px; overflow: visible; }
  .tagline-text {
    font-family: "Yellowtail", cursive; font-size: 60px; fill: var(--white);
  }
</style>
</head>
<body>
<main class="brochure-cover">
  <header class="masthead">
    <div class="brand">
      <span class="brand-square"></span>
      <span class="brand-name">Velorquintade</span>
    </div>
    <div class="contact">
      <p>Request a Call 0491 570 156</p>
      <p>www.velorquintade.com.au</p>
    </div>
  </header>

  <div class="hero-photo" role="img" aria-label="Photo of rooftop solar panels reflecting a cloudy evening sky"></div>

  <h1 class="headline">Energy solutions<br>for a changing world</h1>

  <svg class="tagline" width="1200" height="112" viewBox="0 0 1200 112">
    <defs>
      <filter id="tagline-shadow" x="-5%" y="-30%" width="110%" height="160%">
        <feDropShadow dx="3" dy="4" stdDeviation="2.5" flood-color="#000" flood-opacity="0.75"/>
      </filter>
    </defs>
    <rect x="0" y="12" width="1200" height="29" fill="var(--band-yellow)"/>
    <rect x="0" y="41" width="1200" height="30" fill="var(--band-green)"/>
    <rect x="0" y="71" width="1200" height="29" fill="var(--band-blue)"/>
    <text class="tagline-text" x="55" y="74" textLength="1092" lengthAdjust="spacingAndGlyphs" filter="url(#tagline-shadow)">We pride ourselves on providing premium quality solar services</text>
  </svg>
</main>
</body>
</html>
```